New Website for Manufacturing Company - PSD only, no coding - CLOSED TO NEW DESIGNERS

IF YOU HAVE NOT ALREADY SUBMITTED A DESIGN PLEASE DO NOT SUBMIT ONE.
This is a re-work of an existing website. We can keep the themes and color schemes the same but we will be changing the layout and page content.
The scope includes the creation of some icons/sketches that will form some of the page content.
The scope is design only, no coding.
There are four files that have been uploaded that give a more detailed project brief, please read them.
Target Market(s)
Manufacturing
Industry/Entity Type
It Company
Number of Pages Required
1 page
Look and feel
Each slider illustrates characteristics of the customer's brand and the style your logo design should communicate.

```html
<!DOCTYPE html>
<html lang="en">
<head>
<meta charset="utf-8">
<title>Corvale Manufacturing — High Temperature Insulation Experts</title>
<link href="https://fonts.googleapis.com/css2?family=Open+Sans:ital,wght@0,400;0,600;0,700;0,800;1,400;1,600&display=swap" rel="stylesheet">
<style>
:root{
  --blue:#1f6fb8;
  --blue-dark:#17599a;
  --blue-light:#4a97d8;
  --navy:#0f2740;
  --navy-deep:#0a1c2f;
  --red:#d8262b;
  --text:#56606b;
  --muted:#8a949e;
  --line:#d9dee3;
  --panel:#f1f3f5;
  --white:#ffffff;
}
*{box-sizing:border-box;margin:0;padding:0}
html,body{width:893px;height:1200px;overflow:hidden}
body{font-family:"Open Sans",Arial,sans-serif;color:var(--text);background:var(--white);position:relative}
.wrap{width:570px;margin:0 auto;position:relative}

/* header */
.site-header{height:70px}
.site-header .wrap{display:flex;align-items:center;height:70px;justify-content:space-between}
.brand{display:flex;align-items:center;gap:10px}
.brand-name{font-weight:800;color:var(--blue);font-size:19px;letter-spacing:.5px;line-height:1}
.brand-sub{font-size:7px;font-weight:700;color:var(--blue);letter-spacing:1px;display:block;margin-top:2px}
.tagline{font-size:10px;color:var(--blue);line-height:1.3;border-left:1px solid var(--line);padding-left:10px}
.header-contact{font-size:10px;color:var(--text);line-height:1.7}
.header-contact div{display:flex;align-items:center;gap:6px}
.header-contact svg{width:11px;height:11px}

/* nav */
.main-nav{background:var(--blue);height:28px}
.main-nav ul{list-style:none;display:flex;height:28px;align-items:center;gap:2px}
.main-nav li{font-size:8px;font-weight:700;color:var(--white);padding:0 12px;height:28px;display:flex;align-items:center}
.main-nav li.active{background:var(--blue-dark)}
.main-nav li.rfq{background:var(--red);height:16px;border-radius:2px;margin:0 6px;padding:0 10px}

/* hero */
.hero{height:232px;background:linear-gradient(135deg,#2e84cf 0%,#1d65aa 55%,#164f8a 100%);position:relative;overflow:hidden}
.hero-media{position:absolute;left:160px;top:22px;width:250px;height:190px;border-radius:6px;background:radial-gradient(ellipse at 50% 50%,#e9edf1 0%,#c5ced6 55%,rgba(197,206,214,0) 80%)}
.hero-copy{position:absolute;left:475px;top:58px;width:260px;color:var(--white)}
.hero-copy h1{font-size:18px;font-weight:400;font-style:italic;line-height:1.25}
.hero-copy h1 strong{font-weight:700}
.hero-btn{display:inline-block;margin-top:14px;background:var(--navy);color:var(--white);font-size:7px;font-weight:700;padding:6px 10px;border-radius:2px;letter-spacing:.3px}
.hero-dots{position:absolute;left:568px;bottom:16px;display:flex;gap:4px}
.hero-dots span{width:5px;height:5px;border-radius:50%;background:rgba(255,255,255,.5)}
.hero-dots span:first-child{background:var(--white)}

/* intro */
.intro{text-align:center;padding:32px 0 0}
.intro h2{font-size:13px;font-style:italic;font-weight:600;color:var(--blue)}
.intro p{font-size:8.5px;line-height:1.6;color:var(--muted);width:470px;margin:10px auto 0}

/* capabilities */
.capabilities{text-align:center;padding-top:36px}
.capabilities h2{font-size:19px;font-weight:400;color:var(--navy);letter-spacing:.5px}
.capabilities h2 b{color:var(--blue);font-weight:800}
.cap-grid{display:grid;grid-template-columns:repeat(4,90px);gap:18px 30px;justify-content:center;margin-top:18px}
.cap-card{height:118px;border:1px solid var(--line);background:var(--white);display:flex;flex-direction:column;align-items:center;justify-content:flex-end;padding-bottom:10px}
.cap-art{width:56px;height:52px;border-radius:4px;background:linear-gradient(160deg,#dfe6ec,#aebcc8);margin-bottom:14px}
.cap-card span{font-size:7.5px;color:var(--text)}
.cap-card.services{background:var(--blue);border-color:var(--blue);justify-content:center;color:var(--white)}
.cap-card.services strong{font-size:9px;display:block}
.cap-card.services span{color:#d7e8f7;font-size:7px;line-height:1.5;margin-top:4px}

/* partners */
.partners{background:var(--panel);height:48px;margin-top:26px;display:flex;align-items:center;justify-content:center;gap:32px}
.partners i{display:block;background:#b8c0c7;border-radius:3px;height:14px}

/* footer */
.site-footer{background:var(--navy);position:absolute;left:0;right:0;top:845px;height:312px;color:#9fb0c1}
.foot-cols{display:grid;grid-template-columns:repeat(6,1fr);gap:12px;padding-top:26px}
.foot-cols h4{font-size:7.5px;font-weight:700;color:var(--blue-light);margin-bottom:7px;letter-spacing:.3px}
.foot-cols li{list-style:none;font-size:6.5px;line-height:1.75}
.foot-divider{border-top:1px solid #213c58;margin-top:20px}
.foot-brand{text-align:center;margin-top:18px;font-weight:800;font-size:17px;color:var(--white);letter-spacing:.5px}
.foot-brand small{display:block;font-size:6px;font-weight:700;letter-spacing:1px;color:#9fb0c1}
.foot-bottom{display:flex;align-items:center;justify-content:space-between;margin-top:14px;font-size:6.5px;line-height:1.6}
.foot-bottom .addr strong{color:var(--white)}
.question{display:flex;align-items:center;gap:12px}
.question .ask small{display:block;color:#f2b84b;font-size:6.5px}
.question .ask b{color:var(--white);font-size:11px}
.chat-btn{background:var(--red);color:var(--white);font-weight:700;font-size:7px;padding:6px 12px;border-radius:2px}
.legal{text-align:right}
.base-strip{position:absolute;left:0;right:0;top:1157px;height:43px;background:var(--navy-deep)}
</style>
</head>
<body>

<header class="site-header">
  <div class="wrap">
    <div class="brand">
      <div class="brand-name">CORVALE<span class="brand-sub">MANUFACTURING</span></div>
      <div class="tagline">High Temperature<br>Insulation Experts</div>
    </div>
    <div class="header-contact">
      <div><svg viewBox="0 0 24 24"><path fill="#1f6fb8" d="M6.6 10.8a15 15 0 006.6 6.6l2.2-2.2c.3-.3.7-.4 1-.2 1.1.4 2.3.6 3.6.6.6 0 1 .4 1 1V20c0 .6-.4 1-1 1A17 17 0 013 4c0-.6.4-1 1-1h3.5c.6 0 1 .4 1 1 0 1.3.2 2.5.6 3.6.1.3 0 .7-.2 1z"/></svg>555.014.2200</div>
      <div><svg viewBox="0 0 24 24"><rect x="2" y="5" width="20" height="14" rx="2" fill="#1f6fb8"/><path d="M3 6l9 7 9-7" stroke="#fff" stroke-width="1.6" fill="none"/></svg>sales@corvalemfg.com</div>
    </div>
  </div>
</header>

<nav class="main-nav">
  <div class="wrap">
    <ul>
      <li class="active">HOME</li>
      <li>RODS</li>
      <li>INDUSTRIAL</li>
      <li>CUSTOM MANUFACTURING</li>
      <li>ABOUT US</li>
      <li class="rfq">RFQ</li>
      <li>CONTACT US</li>
    </ul>
  </div>
</nav>

<section class="hero">
  <div class="hero-media" role="img" aria-label="Photo of white high temperature insulation rings and tubes"></div>
  <div class="hero-copy">
    <h1>Manufacturer, Fabricator and Distributor of <strong>High Temperature</strong> Insulating Materials</h1>
    <span class="hero-btn">VIEW OUR PRODUCTS</span>
  </div>
  <div class="hero-dots"><span></span><span></span></div>
</section>

<section class="intro">
  <h2>"High Temperature Insulation Experts"</h2>
  <p>We shape, cut and finish heat resistant materials for furnaces, kilns, foundries and process lines across many industries. Our team works from your drawing or sample to deliver parts that fit, last and ship on time. Ask about custom runs, short lead times and full material support for every project you bring to us.</p>
</section>

<section class="capabilities">
  <h2><b>OUR</b> CAPABILITIES</h2>
  <div class="cap-grid">
    <div class="cap-card"><div class="cap-art" role="img" aria-label="Sketch of material cutting"></div><span>Material Cutting</span></div>
    <div class="cap-card"><div class="cap-art" role="img" aria-label="Sketch of coating"></div><span>Coating</span></div>
    <div class="cap-card"><div class="cap-art" role="img" aria-label="Sketch of laminating"></div><span>Laminating</span></div>
    <div class="cap-card"><div class="cap-art" role="img" aria-label="Sketch of CNC machining"></div><span>CNC Machining</span></div>
    <div class="cap-card"><div class="cap-art" role="img" aria-label="Sketch of slitting"></div><span>Slitting</span></div>
    <div class="cap-card"><div class="cap-art" role="img" aria-label="Sketch of die cutting"></div><span>Die Cutting</span></div>
    <div class="cap-card"><div class="cap-art" role="img" aria-label="Sketch of vacuum forming"></div><span>Vacuum Forming</span></div>
    <div class="cap-card services"><strong>SERVICES</strong><span>VIEW<br>INDUSTRIAL<br>CAPABILITIES</span></div>
  </div>
</section>

<div class="partners" aria-label="Client badges">
  <i style="width:44px"></i><i style="width:48px"></i><i style="width:56px"></i><i style="width:40px"></i><i style="width:30px"></i><i style="width:44px"></i><i style="width:36px"></i>
</div>

<footer class="site-footer">
  <div class="wrap">
    <div class="foot-cols">
      <div><h4>CAPABILITIES</h4><ul><li>Material Cutting</li><li>Coating</li><li>Laminating</li><li>CNC Machining</li><li>Slitting</li><li>Die Cutting</li><li>Vacuum Forming</li></ul></div>
      <div><h4>SERVICES</h4><ul><li>Design</li><li>Prototyping</li><li>Kitting</li><li>Assembly</li></ul></div>
      <div><h4>MARKETS</h4><ul><li>Aerospace</li><li>Glass</li><li>Metals</li><li>Petrochemical</li><li>Power</li></ul></div>
      <div><h4>MATERIALS</h4><ul><li>Ceramic Fiber</li><li>Mica Sheet</li><li>Gaskets</li><li>Textiles</li><li>Refractory</li></ul></div>
      <div><h4>DOCUMENTATION</h4><ul><li>Data Sheets</li><li>MSDS</li><li>Certifications</li><li>Terms &amp; Conditions</li></ul></div>
      <div><h4>CONTACT US</h4><ul><li>Request Quote</li><li>Directions</li><li>Careers</li></ul></div>
    </div>
    <div class="foot-divider"></div>
    <div class="foot-brand">CORVALE<small>MANUFACTURING</small></div>
    <div class="foot-bottom">
      <div class="addr"><strong>Corvale Manufacturing</strong><br>12 Foundry Street<br>Lakeport, MA 01904</div>
      <div>Tel: 555.014.2200<br>Fax: 555.014.2211<br>sales@corvalemfg.com</div>
      <div class="question">
        <div class="ask"><small>Have Questions?</small><b>555.014.2200</b></div>
        <span class="chat-btn">LIVE CHAT</span>
      </div>
      <div class="legal">© 2024 Corvale Manufacturing<br>All rights reserved.</div>
    </div>
  </div>
</footer>
<div class="base-strip"></div>

</body>
</html>
```